Powepoint Templates From Logo

We need 3 Powerpoint templates for use in a variety of presentations we develop and customize. Primary uses of the powerpoint presentations are for printed "pitch books" describing our firm's capabilities and approach (a lot of words with some design elements that we have developed), printed presentations of the results of financial evaluations of our clients (lots of charts and graphs) and as the talking points for speeches.

The design needs to be professional and "solid" to establish that we are capable of selling your multi-million dollar business, but also be a little different to show that we are not just boring MBA's.

Our current website and other materials have been developed internally and leave a great deal to be desired. I have initiated this project to demonstrate how much our look can be improved and, if successful, I hope to do much bigger projects in the future.
Updates

This is my first project and I thaank you all for your participation. Since I am new to this, I don;t know if I am providing the help and feedback as I should. Please feel free to let me know how I can be a better customer.

Target Market(s)

professionals (lawyers, accountaants), business owners, business groups, technology people

Industry/Entity Type

Financial

Requirements
Must have
• our logo
a place where logo of client can be inserted if appropriate
templates for the following pages
title page
standard bullet narrative page
page for charts and graphs to mostly fill the page
Should not have a lot of dark solid color that has to be printed.

Nice to have
• something to perk up the color a little

```html
<!DOCTYPE html>
<html lang="en">
<head>
<meta charset="utf-8">
<title>Halvern Advisory – Presentation Templates</title>
<link href="https://fonts.googleapis.com/css2?family=Roboto+Condensed:wght@400;700&family=Arimo:wght@400&display=swap" rel="stylesheet">
<style>
  :root{
    --canvas:#e4e5e8;
    --navy:#1f2f5e;
    --navy-deep:#0f1a4b;
    --blue-bright:#1f7fd4;
    --blue-soft:#4aa3e6;
    --title-navy:#1d2c5c;
    --rule:#8f97ad;
    --ink:#1a1a1a;
    --white:#ffffff;
    --bar-blue:#9fb7d6;
    --bar-green:#58b25a;
    --line-orange:#f0a020;
    --line-red:#c0282d;
  }
  *{box-sizing:border-box;margin:0;padding:0}
  html,body{width:1200px;height:900px;overflow:hidden;background:var(--canvas)}
  .canvas{position:relative;width:1200px;height:900px}
  .slide{position:absolute;width:546px;height:410px;overflow:hidden;background:var(--white)}
  .slide--dark{background:var(--navy)}
  .slide--title{left:40px;top:40px}
  .slide--bullets{left:608px;top:40px}
  .slide--chart{left:40px;top:470px}
  .slide--closing{left:608px;top:470px}
  .swoosh{position:absolute;left:0;bottom:0;width:546px;height:410px;pointer-events:none}

  .brand{position:absolute;display:flex;align-items:center;gap:8px;white-space:nowrap;
    font-family:"Roboto Condensed",sans-serif;font-weight:700;color:var(--white);font-size:17px;letter-spacing:.4px}
  .brand__mark{width:19px;height:19px;border:2px solid var(--white);flex:none}
  .slide--title .brand{left:62px;top:166px}
  .slide--closing .brand{left:42px;top:186px}

  .divider{position:absolute;width:2px;background:linear-gradient(to bottom,rgba(255,255,255,0),rgba(255,255,255,.55),rgba(255,255,255,0));
    box-shadow:-18px 0 40px 10px rgba(10,18,50,.45)}
  .slide--title .divider{left:282px;top:132px;height:156px}
  .slide--closing .divider{left:258px;top:128px;height:150px}

  .deck-title{position:absolute;left:296px;top:160px;font-family:"Roboto Condensed",sans-serif;font-weight:700;
    color:var(--white);font-size:33px;line-height:37px}
  .deck-subtitle{position:absolute;left:297px;top:246px;font-family:"Roboto Condensed",sans-serif;
    color:var(--white);font-size:15px;letter-spacing:.3px}
  .thanks{position:absolute;left:314px;top:184px;font-family:"Roboto Condensed",sans-serif;font-weight:700;
    color:var(--white);font-size:32px}

  .page-title{position:absolute;left:38px;top:14px;font-family:"Roboto Condensed",sans-serif;font-weight:700;
    color:var(--title-navy);font-size:25px}
  .page-rule{position:absolute;left:0;top:54px;width:474px;height:1px;background:var(--rule)}

  .body-copy{position:absolute;font-family:Arimo,Arial,sans-serif;font-size:12px;line-height:14.6px;color:var(--ink);text-align:justify}
  .slide--bullets .body-copy{left:48px;top:94px;width:180px}
  .slide--chart .body-copy{left:312px;top:78px;width:178px}

  .bullets{position:absolute;left:262px;top:94px;width:198px;list-style:none;
    font-family:Arimo,Arial,sans-serif;font-size:12px;line-height:14.6px;color:var(--ink)}
  .bullets li{position:relative;padding-left:20px;margin-bottom:13px}
  .bullets li::before{content:"";position:absolute;left:0;top:2px;width:10px;height:10px;border:1.5px solid var(--title-navy)}

  .chart{position:absolute;left:24px;top:78px;width:282px;height:240px}
</style>
</head>
<body>
<main class="canvas">

  <!-- Title page -->
  <section class="slide slide--dark slide--title">
    <div class="brand"><span class="brand__mark"></span>HALVERN ADVISORY</div>
    <div class="divider"></div>
    <h1 class="deck-title">LOREM IPSUM<br>DOLOR SIT AMET</h1>
    <p class="deck-subtitle">Lorem Ipsum Dolor sit Amet</p>
    <svg class="swoosh" viewBox="0 0 546 410" aria-hidden="true">
      <path d="M0,374 C180,380 400,360 546,320 L546,410 L0,410 Z" fill="#172552"/>
      <path d="M0,382 C200,388 410,372 546,340 L546,410 L0,410 Z" fill="var(--navy-deep)"/>
      <path d="M170,410 C320,385 450,350 546,318 L546,332 C450,362 330,395 240,410 Z" fill="var(--blue-bright)"/>
      <path d="M300,410 C400,385 480,360 546,345" stroke="var(--blue-soft)" stroke-width="1.5" fill="none"/>
    </svg>
  </section>

  <!-- Bullet narrative page -->
  <section class="slide slide--bullets">
    <h2 class="page-title">Lorem Ipsum Dolor Sit Amet</h2>
    <div class="page-rule"></div>
    <p class="body-copy">Lorem ipsum dolor sit amet, consectetur adipisicing elit, sed do eiusmod tempor incididunt ut labore et dolore magna aliqua. Ut enim ad minim veniam, quis nostrud exercitation ullamco laboris nisi ut aliquip ex ea commodo consequat. Duis aute irure dolor in reprehenderit in voluptate velit esse cillum dolore eu fugiat nulla pariatur. Excepteur sint occaecat cupidatat non proident, sunt in culpa qui officia deserunt mollit anim id est laborum</p>
    <ul class="bullets">
      <li>Lorem ipsum dolor sit amet, consectetur adipisicing elit,</li>
      <li>sed do eiusmod tempor incididunt ut labore et dolore magna aliqua.</li>
      <li>Ut enim ad minim veniam, quis nostrud exercitation ullamco laboris nisi ut aliquip ex ea commodo consequat.</li>
      <li>Duis aute irure dolor in reprehenderit in voluptate velit esse cillum dolore</li>
    </ul>
    <svg class="swoosh" viewBox="0 0 546 410" aria-hidden="true">
      <path d="M0,372 C180,378 400,358 546,322 L546,410 L0,410 Z" fill="#24346a"/>
      <path d="M0,380 C200,386 410,370 546,342 L546,410 L0,410 Z" fill="var(--navy-deep)"/>
      <path d="M170,410 C320,385 450,350 546,318 L546,332 C450,362 330,395 240,410 Z" fill="var(--blue-bright)"/>
      <path d="M300,410 C400,385 480,360 546,345" stroke="var(--blue-soft)" stroke-width="1.5" fill="none"/>
    </svg>
  </section>

  <!-- Chart page -->
  <section class="slide slide--chart">
    <h2 class="page-title">Lorem Ipsum Dolor Sit Amet</h2>
    <div class="page-rule"></div>
    <svg class="chart" viewBox="0 0 282 240" role="img" aria-label="Bar and line chart of sales employees, bonus versus sales year to date">
      <text x="141" y="10" text-anchor="middle" font-family="Arimo,Arial,sans-serif" font-size="7" font-weight="700" fill="#222">Sales Employees - Bonus vs. SalesYTD</text>
      <g stroke="#c9c9c9" stroke-width=".6">
        <line x1="40" y1="20" x2="270" y2="20"/><line x1="40" y1="50" x2="270" y2="50"/>
        <line x1="40" y1="80" x2="270" y2="80"/><line x1="40" y1="110" x2="270" y2="110"/>
        <line x1="40" y1="140" x2="270" y2="140"/>
      </g>
      <line x1="40" y1="170" x2="270" y2="170" stroke="#777" stroke-width=".8"/>
      <line x1="40" y1="20" x2="40" y2="170" stroke="#777" stroke-width=".8"/>
      <g font-family="Arimo,Arial,sans-serif" font-size="5" fill="#444" text-anchor="end">
        <text x="37" y="22">100 %</text><text x="37" y="52">80 %</text><text x="37" y="82">60 %</text>
        <text x="37" y="112">40 %</text><text x="37" y="142">20 %</text><text x="37" y="172">0 %</text>
      </g>
      <g fill="var(--bar-blue)">
        <rect x="42.2" y="57.5" width="5" height="112.5"/><rect x="57.5" y="77" width="5" height="93"/>
        <rect x="72.8" y="84.5" width="5" height="85.5"/><rect x="88.2" y="92" width="5" height="78"/>
        <rect x="103.5" y="92" width="5" height="78"/><rect x="118.8" y="102.5" width="5" height="67.5"/>
        <rect x="134.2" y="110" width="5" height="60"/><rect x="149.5" y="113" width="5" height="57"/>
        <rect x="164.8" y="117.5" width="5" height="52.5"/><rect x="180.2" y="119" width="5" height="51"/>
        <rect x="195.5" y="125" width="5" height="45"/><rect x="210.8" y="128" width="5" height="42"/>
        <rect x="226.2" y="137" width="5" height="33"/><rect x="241.5" y="155" width="5" height="15"/>
        <rect x="256.8" y="161" width="5" height="9"/>
      </g>
      <g fill="var(--bar-green)">
        <rect x="48.2" y="113" width="5" height="57"/><rect x="63.5" y="120.5" width="5" height="49.5"/>
        <rect x="78.8" y="62" width="5" height="108"/><rect x="94.2" y="125" width="5" height="45"/>
        <rect x="109.5" y="72.5" width="5" height="97.5"/><rect x="124.8" y="98" width="5" height="72"/>
        <rect x="140.2" y="128" width="5" height="42"/><rect x="155.5" y="110" width="5" height="60"/>
        <rect x="170.8" y="101" width="5" height="69"/><rect x="186.2" y="92" width="5" height="78"/>
        <rect x="201.5" y="87.5" width="5" height="82.5"/><rect x="216.8" y="57.5" width="5" height="112.5"/>
        <rect x="232.2" y="87.5" width="5" height="82.5"/><rect x="247.5" y="132.5" width="5" height="37.5"/>
        <rect x="262.8" y="122" width="5" height="48"/>
      </g>
      <polyline fill="none" stroke="var(--line-orange)" stroke-width="1.6"
        points="47.7,152 63,132.5 78.3,113 93.7,95 109,80 124.3,68 139.7,57.5 155,48.5 170.3,41 185.7,35 201,30.5 216.3,26 231.7,23 247,21.5 262.3,20"/>
      <g fill="var(--line-red)">
        <circle cx="47.7" cy="152" r="1.3"/><circle cx="63" cy="132.5" r="1.3"/><circle cx="78.3" cy="113" r="1.3"/>
        <circle cx="93.7" cy="95" r="1.3"/><circle cx="109" cy="80" r="1.3"/><circle cx="124.3" cy="68" r="1.3"/>
        <circle cx="139.7" cy="57.5" r="1.3"/><circle cx="155" cy="48.5" r="1.3"/><circle cx="170.3" cy="41" r="1.3"/>
        <circle cx="185.7" cy="35" r="1.3"/><circle cx="201" cy="30.5" r="1.3"/><circle cx="216.3" cy="26" r="1.3"/>
        <circle cx="231.7" cy="23" r="1.3"/><circle cx="247" cy="21.5" r="1.3"/><circle cx="262.3" cy="20" r="1.3"/>
      </g>
      <polyline fill="none" stroke="var(--line-red)" stroke-width="1.4" stroke-dasharray="4 2"
        points="47.7,158 63,143 78.3,137 93.7,137 109,125 124.3,110 139.7,102.5 155,92 170.3,80 185.7,68 201,57.5 216.3,47 231.7,35 247,24.5 262.3,20"/>
      <rect x="48" y="22" width="42" height="26" fill="#fbf4b0" stroke="#999" stroke-width=".5"/>
      <g font-family="Arimo,Arial,sans-serif" font-size="4.2" fill="#333">
        <rect x="51" y="25" width="4" height="3" fill="var(--bar-blue)"/><text x="57" y="28">Bonus</text>
        <rect x="51" y="31" width="4" height="3" fill="var(--bar-green)"/><text x="57" y="34">Sales</text>
        <line x1="51" y1="38.5" x2="55" y2="38.5" stroke="var(--line-orange)"/><text x="57" y="40">Bonus %</text>
        <line x1="51" y1="44.5" x2="55" y2="44.5" stroke="var(--line-red)" stroke-dasharray="1.5 1"/><text x="57" y="46">Sales %</text>
      </g>
      <g font-family="Arimo,Arial,sans-serif" font-size="4.5" fill="#444" text-anchor="end">
        <text transform="translate(49.5,174) rotate(-90)">Rep 01</text>
        <text transform="translate(64.8,174) rotate(-90)">Rep 02</text>
        <text transform="translate(80.1,174) rotate(-90)">Rep 03</text>
        <text transform="translate(95.5,174) rotate(-90)">Rep 04</text>
        <text transform="translate(110.8,174) rotate(-90)">Rep 05</text>
        <text transform="translate(126.1,174) rotate(-90)">Rep 06</text>
        <text transform="translate(141.5,174) rotate(-90)">Rep 07</text>
        <text transform="translate(156.8,174) rotate(-90)">Rep 08</text>
        <text transform="translate(172.1,174) rotate(-90)">Rep 09</text>
        <text transform="translate(187.5,174) rotate(-90)">Rep 10</text>
        <text transform="translate(202.8,174) rotate(-90)">Rep 11</text>
        <text transform="translate(218.1,174) rotate(-90)">Rep 12</text>
        <text transform="translate(233.5,174) rotate(-90)">Rep 13</text>
        <text transform="translate(248.8,174) rotate(-90)">Rep 14</text>
        <text transform="translate(264.1,174) rotate(-90)">Rep 15</text>
      </g>
    </svg>
    <p class="body-copy">Lorem ipsum dolor sit amet, consectetur adipisicing elit, sed do eiusmod tempor incididunt ut labore et dolore magna aliqua. Ut enim ad minim veniam, quis nostrud exercitation ullamco laboris nisi ut aliquip ex ea commodo consequat. Duis aute irure dolor in reprehenderit in voluptate velit esse cillum dolore eu fugiat nulla pariatur. Excepteur sint occaecat cupidatat non proident, sunt in culpa qui officia deserunt mollit anim id est laborum</p>
    <svg class="swoosh" viewBox="0 0 546 410" aria-hidden="true">
      <path d="M0,372 C180,378 400,358 546,322 L546,410 L0,410 Z" fill="#24346a"/>
      <path d="M0,380 C200,386 410,370 546,342 L546,410 L0,410 Z" fill="var(--navy-deep)"/>
      <path d="M170,410 C320,385 450,350 546,318 L546,332 C450,362 330,395 240,410 Z" fill="var(--blue-bright)"/>
      <path d="M300,410 C400,385 480,360 546,345" stroke="var(--blue-soft)" stroke-width="1.5" fill="none"/>
    </svg>
  </section>

  <!-- Closing page -->
  <section class="slide slide--dark slide--closing">
    <div class="brand"><span class="brand__mark"></span>HALVERN ADVISORY</div>
    <div class="divider"></div>
    <p class="thanks">THANK YOU</p>
    <svg class="swoosh" viewBox="0 0 546 410" aria-hidden="true">
      <path d="M0,374 C180,380 400,360 546,320 L546,410 L0,410 Z" fill="#172552"/>
      <path d="M0,382 C200,388 410,372 546,340 L546,410 L0,410 Z" fill="var(--navy-deep)"/>
      <path d="M170,410 C320,385 450,350 546,318 L546,332 C450,362 330,395 240,410 Z" fill="var(--blue-bright)"/>
      <path d="M300,410 C400,385 480,360 546,345" stroke="var(--blue-soft)" stroke-width="1.5" fill="none"/>
    </svg>
  </section>

</main>
</body>
</html>
```